DM - management consultant

Business card - contemporary design

Front info
Dorian Maples

(Address not necessary)
PO Box 7386
Alder Ridge, CA 94990

(650) 555-0143
dm@dorianmapl.es

Twitter: dmq527
Facebook: /Dorian.Maples
Linkedin: /in/dorianmaples

Back or Front
www.dorianmaples.net
Facilitation & coaching, change management, strategic partnerships, business improvement

Target Market(s)

High tech businesses - mostly startups in Silicon Valley

Industry/Entity Type

Business

Font styles to use
Sans Serif

Colors

Designer to choose colors to be used in the design.

```html
<!DOCTYPE html>
<html lang="en">
<head>
<meta charset="utf-8">
<title>Dorian Maples – Business Card</title>
<link rel="stylesheet" href="https://fonts.googleapis.com/css2?family=Arimo:wght@400;700&display=swap">
<style>
  :root {
    --backdrop: #3a3a3a;
    --card: #ffffff;
    --band-grey: #e6e6e6;
    --ink: #111111;
    --accent-blue: #00a8e8;
    --accent-orange: #e8641c;
    --tab-black: #0b0b0b;
    --on-dark: #ffffff;
  }
  * { margin: 0; padding: 0; box-sizing: border-box; }
  html, body { width: 1200px; height: 1000px; overflow: hidden; }
  body {
    background: var(--backdrop);
    font-family: "Arimo", Arial, sans-serif;
    color: var(--ink);
    position: relative;
  }
  .card {
    position: absolute;
    left: 220px;
    width: 760px;
    height: 440px;
    background: var(--card);
    border-radius: 24px;
    overflow: hidden;
    box-shadow: 0 12px 30px rgba(0,0,0,.45);
  }
  .card--front { top: 50px; }
  .card--back { top: 520px; }

  /* front */
  .band { position: absolute; left: 0; right: 0; background: var(--band-grey); }
  .band--top { top: 90px; height: 50px; }
  .band--middle { top: 150px; height: 100px; }
  .band--lower { top: 262px; height: 138px; }

  .front-name {
    position: absolute; left: 100px; top: 98px;
    font-size: 30px; font-weight: 400;
  }
  .front-name-rule {
    position: absolute; left: 100px; top: 148px;
    width: 255px; height: 2px; background: var(--ink);
  }
  .services {
    position: absolute; left: 205px; top: 156px;
    font-size: 17px; line-height: 22px;
    color: var(--accent-blue);
  }
  .profile-strip {
    position: absolute; left: 440px; right: 0; top: 212px; height: 58px;
    background: var(--accent-orange);
    display: flex; align-items: center; justify-content: flex-end;
    gap: 14px; padding-right: 26px;
    font-size: 17px; color: var(--ink);
  }
  .profile-mark {
    width: 30px; height: 30px; border-radius: 5px;
    background: var(--tab-black);
  }
  .contact-tab {
    position: absolute; left: 50px; top: 285px;
    width: 58px; height: 135px;
    background: var(--tab-black);
    border-radius: 0 14px 14px 0;
    display: flex; flex-direction: column; align-items: center;
    justify-content: space-around; padding: 14px 0;
  }
  .contact-tab svg { width: 30px; height: 30px; }
  .address {
    position: absolute; left: 124px; top: 302px;
    font-size: 18px; line-height: 23px;
  }
  .phone {
    position: absolute; left: 136px; top: 368px;
    font-size: 18px;
  }

  /* back */
  .back-band {
    position: absolute; left: 0; right: 0; top: 120px; height: 132px;
    background: var(--accent-blue);
  }
  .back-name {
    position: absolute; left: 0; right: 0; top: 158px;
    text-align: center;
    font-size: 40px; font-weight: 400;
    text-shadow: 2px 3px 3px rgba(0,0,0,.35);
  }
  .services-pill {
    position: absolute; left: 70px; right: 70px; top: 240px;
    height: 30px; border-radius: 8px;
    background: var(--tab-black); color: var(--on-dark);
    font-size: 15px; line-height: 30px; text-align: center;
  }
  .website {
    position: absolute; left: 0; right: 0; top: 360px;
    text-align: center; font-size: 15px; letter-spacing: .5px;
  }
</style>
</head>
<body>

<section class="card card--front" aria-label="Card front">
  <div class="band band--top"></div>
  <div class="band band--middle"></div>
  <div class="band band--lower"></div>

  <h1 class="front-name">Dorian Maples</h1>
  <div class="front-name-rule"></div>
  <p class="services">Facilitation &amp; coaching | Change management<br>Strategic partnerships &nbsp;| Business improvement</p>

  <div class="profile-strip">
    <span>profilehub.com/in/dorianmaples</span>
    <span class="profile-mark"></span>
  </div>

  <div class="contact-tab">
    <svg viewBox="0 0 30 30" aria-hidden="true" fill="none" stroke="#e8641c" stroke-width="2.4">
      <rect x="3" y="4" width="24" height="22" rx="4"/>
      <path d="M15 22c-4-4.5-6-7.5-6-10a6 6 0 0 1 12 0c0 2.5-2 5.5-6 10z"/>
      <circle cx="15" cy="12" r="2"/>
    </svg>
    <svg viewBox="0 0 30 30" aria-hidden="true" fill="none" stroke="#e8641c" stroke-width="2.4">
      <rect x="7" y="2" width="16" height="26" rx="3"/>
      <line x1="13" y1="24" x2="17" y2="24"/>
    </svg>
  </div>
  <p class="address">PO Box 7386<br>Alder Ridge, CA 94990</p>
  <p class="phone">(650) 555-0143</p>
</section>

<section class="card card--back" aria-label="Card back">
  <div class="back-band"></div>
  <h2 class="back-name">Dorian Maples</h2>
  <p class="services-pill">Facilitation &amp; coaching, change management, strategic partnerships, business improvement</p>
  <p class="website">WWW.DORIANMAPLES.NET</p>
</section>

</body>
</html>
```